LABEL DESIGNS FOR SKINCARE LINE

Hello we are needing 12 label various label designs but would like to see you design ONE. We will pick winner from this and send the rest.
LABEL SIZE -2x7
JAR SIZE IS - 8oz
LOGOS FILES BELOW
https://files.pavorna-share.net/drive/folders/7xk3q-wumTrazPLoqVnnRTZBKHAE2DpLW
INFORMATION FOR LABEL
Calm Dune Hush Whipped Body Sugar Scrub 8oz
Ideal for all Skin Types
Ingredients:
Pure Cane Sugar, Extra Virgin Coconut Oil, Mango Butter, Kukum Butter, Emulsifying Wax, Jojoba Seed Oil, Sweet Almond Oil, Strawberry Essential Oil, and Pomegranate Essential Oil.
Directions to use Body Sugar Scrub:
Apply to wet skin gently in a circular motion on desired body area, hands, feet, legs, arms, etc. Once you have a good scrub, rinse, pat dry, and enjoy soft, hydrated skin. Best to use in the shower. Use between 2-3 times a week if needed.
*Cautions:
(1) Allergy: Approach this product with extreme caution, if you have allergies
(2) Avoid direct contact with eyes
Storage/Shelf Life of Product:
For best results, stir/mix scrub with the wooden or plastic spoon before each use. The shelf life of all sugar scrubs is 6-8 weeks. Keep the product in a cool, dry place, away from hot or heated temperatures.
All Natural, Cruelty-Free, Vegan Free
No Mineral Oil
No Petroleum
No Parabens

```html
<!DOCTYPE html>
<html lang="en">
<head>
<meta charset="utf-8">
<title>Velvet Hollow – Calm Dune Hush Whipped Body Sugar Scrub Label</title>
<link rel="stylesheet" href="https://fonts.googleapis.com/css2?family=Baloo+2:wght@600;700&family=Fraunces:opsz,wght@9..144,800&family=Oswald:wght@300;400&family=Roboto+Condensed:ital,wght@0,300;0,400;0,700;1,300&display=swap">
<style>
  :root {
    --page-bg: #e3e3e3;
    --label-cream: #fde9d6;
    --panel-peach: #f8b99a;
    --accent-orange: #ee6a2f;
    --badge-orange: #f26a33;
    --ink-brown: #4c4038;
    --ink-dark: #1d1d1d;
    --rule: #5a4f48;
    --white: #ffffff;
  }
  * { margin: 0; padding: 0; box-sizing: border-box; }
  html, body { width: 1200px; height: 1200px; overflow: hidden; }
  body { background: var(--page-bg); position: relative; font-family: "Roboto Condensed", sans-serif; }

  .label {
    position: absolute; left: 40px; top: 440px;
    width: 1120px; height: 321px;
    background: var(--label-cream);
    overflow: hidden;
    box-shadow: 0 4px 10px rgba(0,0,0,0.18);
  }
  .label__panel { position: absolute; left: 0; top: 0; width: 400px; height: 321px; }

  .directions { position: absolute; left: 27px; top: 20px; width: 310px; color: var(--ink-dark); }
  .directions h2 { font-family: "Baloo 2", sans-serif; font-weight: 700; font-size: 17px; line-height: 1.1; letter-spacing: -0.2px; }
  .directions p { font-weight: 300; font-size: 14.2px; line-height: 1.42; text-align: justify; }
  .directions h2.storage { margin-top: 3px; }
  .directions p.storage-text { font-style: italic; letter-spacing: -0.3px; }
  .placeholder-left { position: absolute; left: 26px; top: 252px; width: 182px; height: 52px; background: var(--white); }

  .front { position: absolute; left: 360px; top: 0; width: 400px; height: 321px; text-align: center; }
  .brand { position: absolute; left: 0; right: 0; top: 34px; display: flex; justify-content: center; align-items: center; gap: 8px; }
  .brand__name { font-family: "Fraunces", serif; font-weight: 800; font-size: 38px; color: var(--accent-orange); letter-spacing: -0.5px; }
  .brand__dot { width: 9px; height: 9px; border-radius: 50%; background: var(--accent-orange); }
  .title { position: absolute; left: 0; right: 0; top: 105px; font-family: "Baloo 2", sans-serif; font-weight: 700; font-size: 31px; line-height: 1.25; }
  .title__product { color: var(--ink-brown); display: block; }
  .title__type { color: var(--accent-orange); display: block; }
  .skin { position: absolute; left: 0; right: 0; top: 196px; font-family: "Oswald", sans-serif; font-weight: 300; font-size: 23px; color: var(--ink-brown); }
  .claims { position: absolute; left: 110px; width: 350px; top: 237px; margin-left: -70px; border-top: 1px solid var(--rule); border-bottom: 1px solid var(--rule); font-family: "Oswald", sans-serif; font-weight: 300; font-size: 22px; line-height: 30px; color: var(--ink-brown); letter-spacing: -0.3px; }
  .netwt { position: absolute; left: 50%; transform: translateX(-50%); top: 281px; background: var(--badge-orange); color: var(--white); font-family: "Oswald", sans-serif; font-weight: 300; font-size: 16px; line-height: 22px; padding: 0 9px; }

  .info { position: absolute; left: 779px; top: 20px; width: 312px; color: var(--ink-dark); }
  .info h2 { font-family: "Baloo 2", sans-serif; font-weight: 600; font-size: 17px; line-height: 1.1; color: var(--accent-orange); }
  .info .ingredients { font-style: italic; font-weight: 300; font-size: 14px; line-height: 1.45; text-align: justify; letter-spacing: -0.3px; }
  .info h2.cautions { margin-top: 8px; }
  .cautions-list { list-style: none; font-weight: 300; font-size: 14.5px; line-height: 1.4; letter-spacing: -0.3px; }
  .cautions-list li { padding-left: 15px; text-indent: -15px; }
  .cautions-list b { font-weight: 700; font-size: 15.5px; }
  .free-list { list-style: none; margin-top: 8px; font-weight: 300; font-size: 19px; line-height: 1.26; }
  .free-list li::before { content: "\25C6"; font-size: 16px; margin-right: 3px; }
  .placeholder-right { position: absolute; left: 1058px; top: 217px; width: 88px; height: 88px; background: var(--white); margin-left: -60px; }
</style>
</head>
<body>
  <section class="label" aria-label="Calm Dune Hush Whipped Body Sugar Scrub wrap label">
    <svg class="label__panel" viewBox="0 0 400 321" aria-hidden="true">
      <path d="M0 0 H370 C345 40 330 80 358 130 C385 180 360 230 375 270 C382 295 385 310 380 321 H0 Z" fill="var(--panel-peach)"/>
    </svg>

    <div class="directions">
      <h2>Directions to use Body Sugar Scrub:</h2>
      <p>Apply to wet skin gently in a circular motion on desired body area, hands, feet, legs, arms, etc. Once you have a good scrub, rinse, pat dry, and enjoy soft, hydrated skin. Best to use in the shower. Use between 2-3 times a week if needed.</p>
      <h2 class="storage">Storage/Shelf Life of Product:</h2>
      <p class="storage-text">For best results, stir/mix scrub with the wooden or plastic spoon before each use. The shelf life of all sugar scrubs is 6-8 weeks. Keep the product in a cool, dry place, away from hot or heated temperatures.</p>
    </div>
    <div class="placeholder-left"></div>

    <div class="front">
      <div class="brand"><span class="brand__name">Velvet Hollow</span><span class="brand__dot"></span></div>
      <h1 class="title"><span class="title__product">Calm Dune Hush Whipped</span><span class="title__type">Body Sugar Scrub</span></h1>
      <div class="skin">Ideal for all Skin Types</div>
      <div class="claims">ALL NATURAL • CRUELTY FREE • VEGAN FREE</div>
      <div class="netwt">Net Wt. 8oz</div>
    </div>

    <div class="info">
      <h2>Ingredients:</h2>
      <p class="ingredients">Pure Cane Sugar, Extra Virgin Coconut Oil, Mango Butter, Kukum Butter, Emulsifying Wax, Jojoba Seed Oil, Sweet Almond Oil, Strawberry Essential Oil, and Pomegranate Essential Oil.</p>
      <h2 class="cautions">*Cautions:</h2>
      <ol class="cautions-list">
        <li><b>1.</b> Allergy: Approach this product with extreme caution, if you have allergies</li>
        <li><b>2.</b> Avoid direct contact with eyes</li>
      </ol>
      <ul class="free-list">
        <li>No Mineral Oil</li>
        <li>No Parabens</li>
        <li>No Petroleum</li>
      </ul>
    </div>
    <div class="placeholder-right"></div>
  </section>
</body>
</html>
```